依頼詳細
富山県緑浜市「緑浜市議会」で、創生系会派「未来創生党緑浜市議会議員会」を結成し、活動を行ってきましたが、それを市民の皆さんにお伝えするために、会報誌を発行したくコンペ方式でデザインをお願いするものです。
宜しくお願い致します。
記載項目
未来創生党緑浜市議会議員会/090-2846-3317(政調会長森川)/作成料5~10万円
サイズ
B4
ページ数
両面
希望イメージ
シンプル 複雑
単色 カラフル
暗い 明るい
日常 高級
遊び心 厳粛
未来的 伝統的
女性的 男性的
希望する色
赤系、緑系、黄・オレンジ系
納品ファイル
• イラストレーター形式 (.ai)
補足説明
・非常に急いでいます
・ロゴは下記からダウンロードお願いします(ただし、党の広報誌でなく、議会会派の広報誌なので控えめでお願いします)
https://www.midori-sosei.jp/policy-koho
https://www.midori-sosei.jp/introduction2/pdf/logo_type_A.JPG
デザイン案の提示を使用にも情報が不足しているとのご指摘・ご質問を頂きました。

そこで、掲載する内容(タイトル、文章、写真及びキャプション)を1つのWordデータにまとめました。
また、当方において、手書きで記載したレイアウト案図(表面及び裏面)データ2点を合わせて送付します。

なお、デザインの良さと価格を見て採用を決めたいと思いますので、
その点も踏まえてご提案を宜しくお願いします。
本件は12月10日(木)に開始するも、情報が不足しているとのご意見・ご指摘を受けました。
そこで、12月13日(日)夜中に、掲載頂きたい情報(文章や写真及びキャプションなど)を追記したところです。

今般、当該内容について、少しだけ修正を加えました。
修正箇所は分かりやすいように黄色に着色又は黄色の枠で囲ってありますので、ご確認の上、既に提出の方は修正対応頂ければ幸いに存じます。
未提出の方は、今回のデータを元にデザイン案を作成願います。

なお、仮に修正対応されなかったとしても、レイアウトの案をご提示いただいていますので、それでもって、私たちの会派の政務調査会を開催し、採用デザイン案を週明け12月22日(月)に決定する予定です。

以上、宜しくお願い致します。

シンプルで明瞭なデザイン、色使いで、パッと見て目につきやすい印象を受けました。
今回の私たちの目的が、多くの市民の皆さまにご覧頂くことであり、その観点から一番最適であると判断した次第です。

年末の依頼で、皆さまお忙しい中、多くのご提案を頂きました。
そして提案のどれもが、非常に質が高く、驚きと感動をもって全提案を拝見させて頂きました。
残念ながら、選定できるのは1点であり、選定できなかった皆さま方には誠に申し訳ございません。

なお、今回初の会派広報紙の発行、そしてデザイナボの活用であり、今後もし仕事を依頼することがありましたら、その際にはぜひご協力頂ければ幸いに存じます。

皆さまのご健康とご多幸、そして良い年を迎えられるよう祈念申し上げ御礼のコメントとします。
誠にありがとうございました。

```html
<!DOCTYPE html>
<html lang="ja">
<head>
<meta charset="utf-8">
<title>会派広報紙 裏面</title>
<link rel="stylesheet" href="https://fonts.googleapis.com/css2?family=M+PLUS+Rounded+1c:wght@800&family=Noto+Sans+JP:wght@400;700&display=swap">
<style>
:root{
  --green:#1d9a3a;
  --ink:#222;
  --rule:#1d9a3a;
  --line:#444;
  --photo-a:#8a8f86;
  --photo-b:#c9cbc2;
  --paper:#fff;
}
*{box-sizing:border-box;margin:0;padding:0}
html,body{width:848px;height:1200px;overflow:hidden;background:var(--paper)}
body{font-family:"Noto Sans JP",sans-serif;color:var(--ink);position:relative}
.page{position:absolute;inset:0}
.abs{position:absolute}
.top-banner{left:44px;top:40px;width:758px;height:32px;background:var(--green);color:#fff;
  font-family:"M PLUS Rounded 1c",sans-serif;font-weight:800;font-size:17px;text-align:center;line-height:32px;letter-spacing:.5px}
.bottom-band{left:44px;top:1160px;width:758px;height:8px;background:var(--green)}
.sec-head{display:flex;align-items:center;gap:6px;font-family:"M PLUS Rounded 1c",sans-serif;font-weight:800}
.sec-num{color:var(--green);font-size:38px;line-height:1}
.sec-title{line-height:1.3}
.sec-title .main{font-size:15px;display:block}
.sec-title .sub{font-size:12.5px;display:block}
.body-text{font-size:11.6px;line-height:19.4px;text-align:justify}
.body-text p{margin:0}
.photo{float:right;margin:0 0 4px 8px}
.photo-fill{width:100%;background:linear-gradient(160deg,var(--photo-b),var(--photo-a))}
.photo figcaption{font-size:5px;color:#555;text-align:center;line-height:8px}
.hr{background:var(--rule);height:2px}
.vr{background:var(--rule);width:2px}
.subbar{background:var(--green);color:#fff;font-family:"M PLUS Rounded 1c",sans-serif;font-weight:800;
  font-size:19px;text-align:center;line-height:31px;height:31px}
.placeholder{border:1px solid var(--line)}
.placeholder svg{position:absolute;inset:0;width:100%;height:100%}
.placeholder span{position:absolute;left:50%;top:50%;transform:translate(-50%,-50%);background:#fff;font-size:9px;padding:2px 4px}
.stats{border-collapse:collapse;font-size:9px}
.stats th,.stats td{border:1px solid var(--line);height:18.5px;padding:0 6px}
.stats th{font-weight:400;font-size:11px;text-align:center}
.stats td.val{text-align:center;font-size:11.5px}
.notes{font-size:7px;line-height:10px;color:#333}
.roles{font-size:9.2px;line-height:16.3px;color:#333}
</style>
</head>
<body>
<div class="page">

  <div class="abs top-banner">私たちが議会で質問した数は 298 項目に渡ります。</div>

  <!-- Section 4 -->
  <div class="abs sec-head" style="left:62px;top:80px;width:360px">
    <span class="sec-num">4.</span>
    <span class="sec-title"><span class="main">議会改革断行、公正な議会へ！！</span><span class="sub">不適切な政務活動費の使用問題に、厳正に対処。</span></span>
  </div>
  <div class="abs body-text" style="left:64px;top:127px;width:352px">
    <figure class="photo" style="width:132px">
      <div class="photo-fill" role="img" aria-label="会派内会議の様子の写真" style="height:92px"></div>
      <figcaption>令和2.07.30 議会改革検討委員会に向けた会派内会議</figcaption>
    </figure>
    <p>市議会の会派「創生同志会」が令和元年度、会派離脱した 17 人分を含む政務活動費約 200 万円の大半を使用していたことが同年 6 月新聞で報道されました。</p>
    <p>財政健全化の折、緑浜市議会は議員報酬の引き下げと併せ、政務活動費を減額している中、公金に対するより厳正な対応が必要であり、このような問題を二度と繰り返さぬため、議会改革検討委員会の中で政務活動費の使途基準改正を行いました。</p>
    <p>なおこの他、同委員会において、特別委員会のあり方や、議会選出の監査委員の見直しなどについても議論を進めるなどしたところであり、今後も不断の議会改革を進めていきます。</p>
  </div>
  <div class="abs hr" style="left:55px;top:387px;width:356px"></div>

  <div class="abs placeholder" style="left:58px;top:400px;width:347px;height:346px">
    <svg viewBox="0 0 347 346" preserveAspectRatio="none"><line x1="0" y1="0" x2="347" y2="346" stroke="#444"/><line x1="347" y1="0" x2="0" y2="346" stroke="#444"/></svg>
    <span>画像・イラストスペース</span>
  </div>

  <div class="abs vr" style="left:423px;top:80px;height:668px"></div>

  <!-- Section 5 -->
  <div class="abs sec-head" style="left:441px;top:80px;width:360px">
    <span class="sec-num">5.</span>
    <span class="sec-title"><span class="main">政策集団として。政策立案に向け、</span><span class="main">年間通じて研修会や政調会を開催！</span></span>
  </div>
  <div class="abs body-text" style="left:450px;top:127px;width:348px">
    <figure class="photo" style="width:132px">
      <div class="photo-fill" role="img" aria-label="講師を招いた研修会の写真" style="height:92px"></div>
      <figcaption>令和2.02.03「子育て支援について」研修会</figcaption>
    </figure>
    <p>国の政策を捉え、本市行政への活用を図るための中央視察研修 ( 東京 )、緑浜市内に講師を招いての市政課題に係る研修会等、年間通じて研修。なお、議会会派代表質問や、市への要望書作成等、政策立案に向けた「政務調査会」を昨年 11 月会派結成から 1 年間で計 15 回開催。</p>
  </div>
  <div class="abs hr" style="left:436px;top:270px;width:356px"></div>

  <!-- Section 6 -->
  <div class="abs sec-head" style="left:441px;top:280px;width:360px">
    <span class="sec-num">6.</span>
    <span class="sec-title" style="text-align:right;width:305px"><span class="main">本会議「会派代表質問」を通じた</span><span class="main">政策提言、市政発展へ！</span></span>
  </div>
  <div class="abs subbar" style="left:439px;top:329px;width:350px">①会派代表質問とは</div>
  <div class="abs body-text" style="left:439px;top:369px;width:350px">
    <p>緑浜市議会では、改選直後に行われる定例会（通常であれば改選直後の 12 月定例会）と、それ以後に行われる 9 月及び 3 月定例会において、4 人以上の会派に対して会派代表による質問を行う権利が認められています。</p>
    <p>現在、私たちの会派のみがその資格を有しており、議員 16 名の人的ネットワークや知見を結集し、代表質問を行うことで市の発展の実現を図っています。</p>
    <p>補足すると、議員各個人による一般質問より、代表質問は市政運営を行う市当局にとって非常に重いものとなります。</p>
  </div>
  <div class="abs subbar" style="left:439px;top:553px;width:350px">②これまでの代表質問について</div>
  <div class="abs body-text" style="left:439px;top:593px;width:350px">
    <p>令和元年 11 月結成後の翌年令和 2 年 3 月定例会の代表質問では、財政健全化を始め、教育環境整備、中心市街地活性化や緑浜・港北線 LRT 等の検討などについて。</p>
    <p>令和 2 年 9 月定例会の代表質問ではコロナ関連始め、デジタルトランスフォーメーションによる新たな日常の実現（議会のみならず行政の電子化推進）、そして令和元年 12 月に続いての「駅前ミナモビルへの市役所本庁舎等の移転」について、それぞれ市当局に対して質問・提言。（詳細は議会公式 HP を参照下さい）</p>
  </div>

  <div class="abs hr" style="left:55px;top:752px;width:742px"></div>

  <!-- Section 7 -->
  <div class="abs sec-head" style="left:62px;top:774px;width:360px">
    <span class="sec-num">7.</span>
    <span class="sec-title"><span class="main" style="font-size:19px">数字で見る私たちの活動</span></span>
  </div>
  <div class="abs body-text" style="left:62px;top:810px;width:350px">
    <p>上記(1)～(6)に加え、会派所属議員は定例会ごとに市政のチェック及び政策提言を行ってきたほか、新年度予算に対する市への要望、あるいは様々な場面で通年に渡り政策調整を実施。</p>
    <p>なお、これら政策を実現するために必要な議会諸役員の大半を私たちの会派で担っているところであり、その点も含め、下記の通り数値化して表にまとめました。</p>
  </div>

  <table class="abs stats" style="left:437px;top:805px;width:343px">
    <tr><th style="width:250px">内 容</th><th>数 値</th></tr>
    <tr><td>議会「一般質問」での延べ登壇回数※1</td><td class="val">38 回</td></tr>
    <tr><td>令和 2 年度予算に対する要望項目数</td><td class="val">139 件</td></tr>
    <tr><td>令和 3 年度予算に対する要望項目数</td><td class="val">144 件</td></tr>
    <tr><td>当会派で担っている主な議会諸役員数※2</td><td class="val">58</td></tr>
  </table>
  <div class="abs notes" style="left:582px;top:900px;width:200px">※1…会派結成から約 1 年間（R1.11 ～ R2.12 末）の値<br>※2…令和 2 年 12 月末現在の値</div>

  <div class="abs subbar" style="left:61px;top:933px;width:349px;height:32px;line-height:32px">私たちが担う議会諸役員</div>
  <div class="abs roles" style="left:66px;top:971px;width:344px">
    議長 / 副議長 / 議会運営委員会 ( 正副委員長 ) / 総務文教常任委員会 ( 正副委員長 ) / 民生病院常任委員会 ( 正副委員長 ) / 産業建設常任委員会 ( 正副委員長 ) / 港湾・公共交通対策特別委員会 ( 委員長 ) / 歴史文化・観光対策特別委員会 ( 副委員長 ) / まちづくり対策特別委員会 ( 正副委員長 ) / 広報広聴委員会 ( 正副委員長 ) / 議会改革検討委員会 ( 正副委員長 ) / 青川水害予防組合議会議員 / 白石川中流水害予防組合議会議員 / 緑浜地区広域圏事務組合議会議員 / 西野地方衛生施設組合議会議員 / 若葉県後期高齢者医療広域連合議会議員 / 民生委員推薦会委員 / 森野奨学金支給審査委員会委員 / 国際交流協会顧問・理事 / 国民健康保険運営協議会委員 / 産業振興会議委員 / 交通安全対策委員会委員 / 放置自転車対策審議会委員 / 緑化審議会委員 / 農政推進協議会委員 / 総合計画審議会委員 / 都市計画審議会委員 / 土地開発公社参与
  </div>

  <div class="abs placeholder" style="left:437px;top:933px;width:341px;height:216px">
    <svg viewBox="0 0 341 216" preserveAspectRatio="none"><line x1="0" y1="0" x2="341" y2="216" stroke="#444"/><line x1="341" y1="0" x2="0" y2="216" stroke="#444"/></svg>
    <span>画像・イラストスペース</span>
  </div>

  <div class="abs bottom-band"></div>
</div>
</body>
</html>
```